Iconic Festival requires a Joomla 3.x template

Wellmere Carnivals Society Inc is a not-for-profit organisation charged with the responsibility to deliver the iconic Wellmere Pear & Plum Festival.

This festival is held biennially in the town of Wellmere, located on the Northland/New South Wales border in Australia. Since it’s humble beginnings back in 1954, the Pear & Plum Festival (originally known as “Return to Wellmere Days”) is one of Northland’s Iconic Events attracting more than 52,000 visitors over the 3 days of the festival.

The Pear & Plum Festival celebrates the harvest of two of Wellmere and the Stonevale Ridge’s major agricultural industries. The Festival culminates on the weekend with street performers, stalls, bands and a multicultural fiesta in the park celebrating our region’s diversity and the products we are now famous for; primarily wine.

The continued success of the Festival is its ability to adapt and reinvent itself year after year. Wellmere Carnivals Inc is now looking for a new website to reflect this success, the vibrancy of the event and the overall fun to be had.

The next Pear & Plum Harvest Festival will be the golden jubilee (50th anniversary).

Design Vision

Your template design should meet the following design requirements:

• Be designed for Joomla! 3.x CMS

• Vibrant ‘fun’ design reflecting the principles of the Festival - Apples, Grapes, Multiculturalism,
Food, Wine, Music, Entertainment

• Utilise the colours red, green. purple and gold (as it is the golden jubilee)

• Use a clean set of web fonts striking a balance between design and load time

• Have various module positions

• May not be branded by the designer

• Must be responsive

This website will be the online presence for the Festival, so should provide a framework to easily deliver information to visitors wishing to attend. It is essential that the design be compatible with as many browsers and devices as possible to provide a unified experience to all online visitors.

Target Audience(s)

The General Public: The Pear & Plum Harvest Festival appeals to a broad audience from young to old.

Sponsors: The Pear & Plum Harvest Festival could not be possible without the support of sponsors. The template design should feature a somewhat prominent position to display event sponsors to give them recognition for the valued donation.

Business: The Festival attracts a large number of street vendors and stall holders.

Volunteers: Volunteers provide a vital service ensuring the event is a success.

Media: Being an Iconic Event, the Pear & Plum Harvest Festival attracts a large amount of media attention.

Website Activities

The website will provide the following activities you may want to keep in mind when designing your template:

• Blogs (multiple)
• Sponsorship/Donations
• Event Calendar(s)
• Registration Forms
• Historical Collection
• Merchandise & Ticket Sales
• Social Media integration

A collection of images and the festival's logo can be found on dropbox - https://www.filecrate.example/sh/kq7tz20wbnf3x8/BBRRmh_LL2PTXoQwzkdRXYbMd?dl=0
Updates

Target Market(s)

Industry/Entity Type

Festival

Number of Pages Required

1 page

Font styles to use
Sans Serif
Decorative
Script

Requirements
Must have
• • Be designed for Joomla! 3.x CMS
• • Vibrant ‘fun’ design reflecting the principles of the Festival - Apples, Grapes, Multiculturalism,
• Food, Wine, Music, Entertainment
• • Utilise the colours red, green. purple and gold (as it is the golden jubilee)
• • Use a clean set of web fonts striking a balance between design and load time
• • Have various module positions
• • May not be branded by the designer
• • Must be responsive

```html
<!DOCTYPE html>
<html lang="en">
<head>
<meta charset="utf-8">
<title>Pear &amp; Plum Harvest Festival</title>
<link href="https://fonts.googleapis.com/css2?family=Roboto:wght@400;500;700&family=Roboto+Condensed:wght@300;700&family=Fira+Sans:wght@400&display=swap" rel="stylesheet">
<style>
:root{
  --gold:#bf8c0b;
  --navy:#1d2275;
  --red:#d5102a;
  --plum:#3b0d45;
  --green:#1a7a35;
  --tag-green:#2b8a3e;
  --text:#222;
  --rule:#e2e2e2;
  --footer:#ebebeb;
  --white:#fff;
}
*{box-sizing:border-box;margin:0;padding:0}
html,body{width:838px;height:1200px;overflow:hidden;background:var(--white)}
body{position:relative;font-family:"Roboto",sans-serif;color:var(--text)}
.site-header{position:absolute;left:0;top:0;width:838px;height:114px}
.brand{position:absolute;left:70px;top:38px;display:flex;align-items:center;gap:8px;width:130px}
.brand-dot{width:24px;height:24px;border-radius:50%;background:var(--green);flex:none}
.brand-name{font:700 12px/1.25 "Roboto",sans-serif;color:var(--plum)}
.tagline{position:absolute;right:71px;top:33px;text-align:right;color:var(--tag-green);font:400 17px/28px "Roboto",sans-serif}
.main-nav{position:absolute;left:0;top:114px;width:838px;height:34px;background:var(--gold);display:flex;padding-left:63px}
.main-nav a{color:var(--white);text-decoration:none;font:700 9.2px/34px "Roboto",sans-serif;padding:0 9.5px;border-right:1px solid rgba(255,255,255,.18);text-transform:uppercase}
.main-nav a:last-child{border-right:0}
.hero{position:absolute;left:0;top:148px;width:838px;height:364px;background:linear-gradient(120deg,#3c3a36 0%,#6b5f55 25%,#8e2a22 45%,#b52a24 55%,#5d5750 75%,#7b776f 100%)}
.hero-caption{position:absolute;left:110px;top:136px;width:215px;height:96px;background:rgba(20,20,20,.55);padding:11px 16px 0 17px;color:var(--white);font:300 14.2px/25px "Roboto Condensed",sans-serif;text-transform:uppercase;white-space:nowrap}
.hero-arrow{position:absolute;top:162px}
.hero-arrow.prev{left:56px}.hero-arrow.next{left:752px}
.quick-links{position:absolute;top:531px;left:71px;width:696px;height:54px}
.quick-link{position:absolute;top:0;height:54px;display:flex;align-items:center;gap:14px;padding-left:14px;color:var(--white);font:400 14px "Fira Sans",sans-serif;text-decoration:none}
.tickets{left:0;width:175px;background:var(--navy)}
.program{left:184px;width:150px;background:var(--red)}
.stay{left:344px;width:176px;background:var(--plum)}
.shop{left:529px;width:166px;background:var(--green)}
.welcome{position:absolute;left:71px;top:610px;width:696px}
.section-title{font:700 11px "Roboto",sans-serif;color:var(--navy);text-transform:uppercase}
.welcome-copy{position:absolute;left:0;top:25px;width:457px;font:400 9.3px/15.8px "Roboto",sans-serif}
.welcome-copy p+p{margin-top:10px}
.welcome-photo{position:absolute;left:480px;top:29px;width:216px;height:205px;background:linear-gradient(160deg,#8a8f7a,#c9b36b 45%,#c64a5a 70%,#555 100%)}
.rule{position:absolute;left:71px;width:696px;height:1px;background:var(--rule)}
.sponsors{position:absolute;left:0;top:907px;width:838px;text-align:center}
.sponsor-row{position:absolute;top:34px;left:0;width:838px;display:flex;justify-content:center;gap:46px;align-items:center}
.sponsor{display:flex;align-items:center;gap:6px;font:500 11px "Roboto",sans-serif;color:var(--navy)}
.sponsor i{width:22px;height:22px;border-radius:50%;background:#3aa6d9;display:block}
.mailing{position:absolute;left:0;top:1027px;width:838px;text-align:center}
.mail-form{position:absolute;top:34px;left:186px;display:flex;gap:8px}
.mail-form input{width:156px;height:32px;border:1px solid #ccc;padding:0 11px;font:400 9px "Roboto",sans-serif;color:#777}
.mail-form button{margin-left:2px;width:125px;height:32px;border:0;background:var(--gold);color:var(--white);font:700 10.5px "Roboto",sans-serif}
.site-footer{position:absolute;left:0;top:1125px;width:838px;height:75px;background:var(--footer);font:400 9px "Roboto",sans-serif}
.follow{position:absolute;left:71px;top:24px;display:flex;align-items:center;gap:5px}
.follow span{margin-right:5px}
.social{width:17px;height:17px;display:block}
.social.one{background:#2d4f91}.social.two{background:#1c9bd8}
.copyright{position:absolute;right:71px;top:26px}
</style>
</head>
<body>
<header class="site-header">
  <div class="brand"><span class="brand-dot"></span><span class="brand-name">Pear &amp; Plum Harvest Festival</span></div>
  <p class="tagline">3 Big Days, 3 Big Nights<br>7th, 8th and 9th March, 2014</p>
</header>
<nav class="main-nav">
  <a href="#">Whats On</a><a href="#">Young Ambassadors</a><a href="#">Plan Your Trip</a><a href="#">Festival Facts</a><a href="#">Sponsors</a><a href="#">Volunteers</a><a href="#">Media</a><a href="#">Stallholders</a><a href="#">Contact</a>
</nav>
<section class="hero" role="img" aria-label="Festival parade crowd gathered around a giant fruit float">
  <svg class="hero-arrow prev" width="30" height="40" viewBox="0 0 30 40"><path d="M24 4 8 20l16 16" fill="none" stroke="#fff" stroke-width="7"/></svg>
  <div class="hero-caption">The Pear &amp; Plum Festival<br>celebrates the harvest of<br>two of Wellmere</div>
  <svg class="hero-arrow next" width="30" height="40" viewBox="0 0 30 40"><path d="M6 4l16 16L6 36" fill="none" stroke="#fff" stroke-width="7"/></svg>
</section>
<div class="quick-links">
  <a class="quick-link tickets" href="#"><svg width="24" height="24" viewBox="0 0 24 24" fill="none" stroke="#fff" stroke-width="1.4"><path d="M2 4h20M5 4v6h14V4M8 10l1 12M16 10l-1 12M9 16h6"/></svg>Purchase Tickets</a>
  <a class="quick-link program" href="#"><svg width="22" height="22" viewBox="0 0 22 22" fill="none" stroke="#fff" stroke-width="1.4"><rect x="2" y="4" width="18" height="16"/><path d="M2 9h18M6 2v4M16 2v4"/></svg>Program</a>
  <a class="quick-link stay" href="#"><svg width="36" height="30" viewBox="0 0 36 30" fill="#fff"><rect x="2" y="8" width="10" height="22"/><rect x="14" y="0" width="10" height="30"/><rect x="26" y="12" width="9" height="18"/></svg>Accommodation</a>
  <a class="quick-link shop" href="#"><svg width="22" height="22" viewBox="0 0 22 22" fill="none" stroke="#fff" stroke-width="1.4"><rect x="2" y="6" width="18" height="15" rx="2"/><path d="M7 6V4a4 4 0 0 1 8 0v2"/></svg>Merchandise</a>
</div>
<section class="welcome">
  <h2 class="section-title">Welcome to our site</h2>
  <div class="welcome-copy">
    <p>The Pear and Plum harvest festival dates back to 1954 when it was known as the Return to Wellmere Days now it has grown into one of northland iconic events and attracts up to 52000 visitors over its current 3 days of fun. The festival starts with seasonal Harvest Tours &amp; Harvest Feasts on Thursday and friday, pear day events on Friday, progressing to the gala ball on the Friday night, tht street parade and celebrity plum crush on the satuday. The day ends with a fantastic fireworks display over the creek and great entertainment in the main street, finally after you have been partying all right, try the Mt Harrow 10k Callenge and the Tinpail Crek 5k walk on the sunday. THe park hotels a taste of the Stonevale Ridge on both the Saturday and SUnday where you can enjoy local win, cheese, seasonal harvest appreciation Sessions, and swing along to great entertainment throughout the town. The festival is not just for those who have come to sample Wine countrt.</p>
    <p>While in Wellmere, Northlands coldest town with the warmest people, stop and have a look around and see the wonderful attractions the Stonevale ridge is famous for Ferncliff national park, tracke the pyramid walk, may be have a swim in the vreek or have a barbie along the creek.</p>
  </div>
  <div class="welcome-photo" role="img" aria-label="Costumed festival performers with flower pot headpieces"></div>
</section>
<div class="rule" style="top:883px"></div>
<section class="sponsors">
  <h2 class="section-title">Our Sponsor</h2>
  <div class="sponsor-row">
    <span class="sponsor"><i></i>Northland Events Bureau</span>
    <span class="sponsor"><i style="background:#2a2a4a"></i>Northland Government</span>
    <span class="sponsor"><i style="background:#6b2a5a"></i>Upper Vale Regional Council</span>
  </div>
</section>
<div class="rule" style="top:1004px"></div>
<section class="mailing">
  <h2 class="section-title">Join our mailing list</h2>
  <form class="mail-form"><input type="text" placeholder="Name"><input type="email" placeholder="E Mail"><button type="button">SUBSCRIBE</button></form>
</section>
<footer class="site-footer">
  <div class="follow"><span>Follow Us On</span><i class="social one"></i><i class="social two"></i></div>
  <p class="copyright">Copyrights @ 2015 All Rights Reserved</p>
</footer>
</body>
</html>
```